upmarket Hair salon A5 flyer design colour double sided

Phone number 9318 7061
address is shop 3/7 Marlowe pde Ashvale
Hi i am wanting a flyer that is upmarket and elegant for my hair salon Velvet Strands For Hair if any pics of hair must look great.
both side must have logo and contact details on
offer side 1
50% off
style cut and finish
*not valid Saturdays
*expires 31/03/15
*butler salon only
*not valid with any other offers
offer side 2
1/2 head foils or all over colour,
cut and finish
$120
*toners and treatment extra costs
*expires 31/03/15
*butler salon only

```html
<!DOCTYPE html>
<html lang="en">
<head>
<meta charset="utf-8">
<title>Velvet Strands For Hair – A5 Offer Flyer</title>
<link rel="stylesheet" href="https://fonts.googleapis.com/css2?family=Crimson+Text:wght@400;600;700&display=swap">
<style>
  :root {
    --backdrop: #1c1c1c;
    --teal-deep: #0f4f52;
    --teal: #1c7a7c;
    --teal-light: #3aa3a2;
    --white: #ffffff;
    --ink: #1d2a2b;
    --photo-grey-dark: #5a5a5a;
    --photo-grey: #8c8c8c;
    --photo-grey-light: #c9c9c9;
    --photo-skin: #d9b8a2;
    --photo-hair: #3a2a22;
    --serif: "Crimson Text", Georgia, serif;
  }
  * { box-sizing: border-box; margin: 0; padding: 0; }
  html, body { width: 1200px; height: 773px; overflow: hidden; }
  body { background: var(--backdrop); font-family: var(--serif); position: relative; }

  .flyer {
    position: absolute; top: 104px; width: 400px; height: 566px; overflow: hidden;
    background: radial-gradient(circle at 30% 30%, var(--teal-light) 0%, var(--teal) 45%, var(--teal-deep) 100%);
    color: var(--white);
  }
  .flyer--front { left: 150px; }
  .flyer--back { left: 650px; }

  .brand-tab {
    position: absolute; top: 0; right: 0; width: 168px; height: 82px;
    background: var(--white); border-bottom-left-radius: 70px;
    display: flex; align-items: center; justify-content: center; gap: 7px;
    padding-left: 14px;
  }
  .brand-tab__dot { width: 10px; height: 10px; border-radius: 50%; background: var(--teal); flex: none; }
  .brand-tab__name { color: var(--ink); font-size: 17px; font-weight: 600; line-height: 1.05; }

  .contact { font-size: 13px; line-height: 1.45; font-style: normal; }
  .contact__row { display: flex; align-items: center; gap: 6px; }
  .contact svg { width: 11px; height: 11px; fill: var(--white); flex: none; }

  /* Front side */
  .flyer--front .contact { position: absolute; top: 44px; left: 22px; }
  .photo-strips { position: absolute; top: 118px; left: 72px; width: 262px; height: 266px; }
  .photo-strips__strip {
    position: absolute; border: 3px solid var(--white);
    background: linear-gradient(180deg, var(--photo-hair) 0%, var(--photo-skin) 45%, #efe6da 100%);
  }
  .photo-strips__strip:nth-child(1) { left: 0;   top: 40px; width: 62px; height: 226px; }
  .photo-strips__strip:nth-child(2) { left: 66px; top: 0;   width: 62px; height: 246px; }
  .photo-strips__strip:nth-child(3) { left: 132px; top: 20px; width: 62px; height: 236px; }
  .photo-strips__strip:nth-child(4) { left: 198px; top: 56px; width: 62px; height: 196px; }

  .offer { position: absolute; left: 168px; right: 14px; top: 404px; }
  .offer__title { font-size: 26px; font-weight: 600; line-height: 1.1; margin-bottom: 4px; white-space: nowrap; }
  .offer__terms { list-style: none; font-size: 16px; line-height: 1.3; }
  .offer__terms li::before { content: "\25B8"; margin-right: 7px; font-size: 12px; }

  .discount-badge {
    position: absolute; left: 22px; bottom: 30px; width: 86px; height: 86px; border-radius: 50%;
    background: var(--white); color: var(--teal); display: flex; flex-direction: column;
    align-items: center; justify-content: center; font-weight: 700; line-height: 0.9;
  }
  .discount-badge__value { font-size: 30px; }
  .discount-badge__label { font-size: 20px; }

  /* Back side */
  .back-offer { position: absolute; top: 94px; left: 30px; width: 240px; }
  .back-offer__title { font-size: 19px; font-weight: 600; line-height: 1.15; margin-bottom: 8px; }
  .back-offer__terms { list-style: disc; padding-left: 16px; font-size: 13px; line-height: 1.4; }
  .back-offer__price { position: absolute; top: 118px; right: 24px; font-size: 46px; font-weight: 600; line-height: 1; }

  .portrait {
    position: absolute; top: 224px; left: 0; width: 400px; height: 252px;
    background: linear-gradient(90deg, var(--photo-grey) 0%, var(--photo-grey-light) 55%, var(--photo-grey-dark) 85%, #2b2b2b 100%);
  }
  .back-footer {
    position: absolute; left: 0; right: 0; bottom: 0; height: 90px;
    display: flex; align-items: center; justify-content: flex-end; padding-right: 24px;
  }
  .back-footer .contact { font-size: 15px; text-align: right; }
  .back-footer .contact__row { justify-content: flex-end; }
</style>
</head>
<body>

  <section class="flyer flyer--front" aria-label="Offer side 1">
    <div class="brand-tab">
      <span class="brand-tab__dot"></span>
      <span class="brand-tab__name">Velvet Strands<br>For Hair</span>
    </div>

    <address class="contact">
      <div class="contact__row">
        <svg viewBox="0 0 24 24"><path d="M6.6 10.8a15.1 15.1 0 0 0 6.6 6.6l2.2-2.2c.3-.3.7-.4 1-.2 1.1.4 2.3.6 3.6.6.6 0 1 .4 1 1V20c0 .6-.4 1-1 1A17 17 0 0 1 3 4c0-.6.4-1 1-1h3.5c.6 0 1 .4 1 1 0 1.3.2 2.5.6 3.6.1.3 0 .7-.2 1z"/></svg>
        <span>9318 7061</span>
      </div>
      <div class="contact__row">
        <svg viewBox="0 0 24 24"><path d="M12 3 2 12h3v9h5v-6h4v6h5v-9h3z"/></svg>
        <span>shop 3/7 Marlowe pde Ashvale</span>
      </div>
    </address>

    <div class="photo-strips" role="img" aria-label="Portrait of a woman with long glossy curled dark hair, set in staggered vertical strips">
      <div class="photo-strips__strip"></div>
      <div class="photo-strips__strip"></div>
      <div class="photo-strips__strip"></div>
      <div class="photo-strips__strip"></div>
    </div>

    <div class="offer">
      <h2 class="offer__title">Style cut and finish</h2>
      <ul class="offer__terms">
        <li>Not valid Saturdays</li>
        <li>Expires 31/03/15</li>
        <li>Ashvale salon only</li>
      </ul>
    </div>

    <div class="discount-badge">
      <span class="discount-badge__value">50%</span>
      <span class="discount-badge__label">off</span>
    </div>
  </section>

  <section class="flyer flyer--back" aria-label="Offer side 2">
    <div class="brand-tab">
      <span class="brand-tab__dot"></span>
      <span class="brand-tab__name">Velvet Strands<br>For Hair</span>
    </div>

    <div class="back-offer">
      <h2 class="back-offer__title">1/2 head foils or all over colour<br>cut and finish</h2>
      <ul class="back-offer__terms">
        <li>Toners and Treatment extra costs</li>
        <li>Expires 31/03/15</li>
        <li>Ashvale salon only</li>
      </ul>
    </div>
    <div class="back-offer__price">$120</div>

    <div class="portrait" role="img" aria-label="Black and white side profile of a woman with a sleek straight dark bob and fringe"></div>

    <footer class="back-footer">
      <address class="contact">
        <div class="contact__row">
          <span>9318 7061</span>
          <svg viewBox="0 0 24 24"><path d="M6.6 10.8a15.1 15.1 0 0 0 6.6 6.6l2.2-2.2c.3-.3.7-.4 1-.2 1.1.4 2.3.6 3.6.6.6 0 1 .4 1 1V20c0 .6-.4 1-1 1A17 17 0 0 1 3 4c0-.6.4-1 1-1h3.5c.6 0 1 .4 1 1 0 1.3.2 2.5.6 3.6.1.3 0 .7-.2 1z"/></svg>
        </div>
        <div class="contact__row">
          <span>shop 3/7 Marlowe pde Ashvale</span>
          <svg viewBox="0 0 24 24"><path d="M12 3 2 12h3v9h5v-6h4v6h5v-9h3z"/></svg>
        </div>
      </address>
    </footer>
  </section>

</body>
</html>
```